lantern institute of business and technology web site

I need web site for the institute which focus on business courses and computer course it is also for vocation train for employment It is also carear development and advancement .It should have links to online study resource which free
Industry/Entity Type
Business
Number of Pages Required
1 page
Look and feel

```html
<!DOCTYPE html>
<html lang="en">
<head>
<meta charset="utf-8">
<title>Lantern Institute of Business and Technology</title>
<link href="https://fonts.googleapis.com/css2?family=Open+Sans:wght@400;600;700;800&display=swap" rel="stylesheet">
<style>
:root{
  --navy:#1b2a5c;
  --navy-dark:#14204a;
  --orange:#f26c1f;
  --grey-bg:#ececec;
  --text:#555;
  --heading:#222;
  --white:#fff;
  --line:#d6d6d6;
  --blue:#3866b4;
  --client:#2d4f8e;
}
*{box-sizing:border-box;margin:0;padding:0}
html,body{width:756px;height:1200px;overflow:hidden}
body{font-family:"Open Sans",Arial,sans-serif;color:var(--text);background:var(--white);font-size:8px;line-height:1.45}
.site-header{background:var(--navy);height:58px;position:relative}
.brand{position:absolute;left:42px;top:6px;background:var(--white);padding:2px 8px 3px;border-radius:2px}
.brand-name{display:block;color:var(--navy);font-weight:800;font-size:11px;letter-spacing:1px}
.brand-tag{display:block;color:var(--navy);font-size:6px;font-weight:600}
.account{position:absolute;right:42px;top:10px;display:flex;gap:6px}
.btn-sm{font-size:7px;font-weight:700;color:var(--white);padding:3px 10px;text-transform:uppercase}
.btn-login{background:#3c62a8}
.btn-register{background:var(--orange)}
.social{position:absolute;right:42px;top:28px;display:flex;gap:10px}
.social span{width:8px;height:8px;background:#8ea2d0;display:block;border-radius:1px}
.main-nav{position:absolute;left:42px;top:44px;display:flex}
.main-nav a{color:var(--white);text-decoration:none;font-size:7.5px;font-weight:600;padding:2px 10px;text-transform:uppercase}
.main-nav a.active{background:var(--orange)}
.hero{height:270px;position:relative;text-align:center;color:var(--white)}
.hero-photo{position:absolute;inset:0;background:radial-gradient(ellipse at 55% 60%,#3d5a8c 0%,#223a68 45%,#131f3d 100%)}
.hero-content{position:relative;padding-top:96px}
.hero h1{font-size:25px;font-weight:800;letter-spacing:.5px}
.hero p{font-size:13px;margin-top:6px}
.hero-actions{margin-top:22px;display:flex;justify-content:center;gap:12px}
.btn{font-size:7px;font-weight:700;color:var(--white);padding:5px 13px;text-transform:uppercase}
.btn-dark{background:var(--navy-dark)}
.btn-orange{background:var(--orange)}
.section-title{text-align:center;color:var(--heading);font-size:15px;font-weight:700;text-transform:uppercase}
.section-title::after{content:"";display:block;width:40px;height:2px;background:var(--orange);margin:6px auto 0}
.welcome{height:112px;padding:28px 140px 0;text-align:center}
.welcome p{margin-top:12px;font-size:7.5px}
.services{background:var(--grey-bg);height:260px;padding-top:22px}
.service-list{display:flex;justify-content:center;gap:20px;margin-top:22px}
.service{width:96px;text-align:center}
.service-icon{width:40px;height:40px;border-radius:50%;background:var(--navy);margin:0 auto;display:flex;align-items:center;justify-content:center}
.service-icon.highlight{background:var(--orange)}
.service h3{font-size:7.5px;color:var(--heading);font-weight:700;margin-top:10px;height:22px}
.service h3.highlight{color:var(--orange)}
.service p{font-size:7px}
.feedback{height:190px;display:flex;padding:28px 42px 0;gap:40px}
.testimonials,.clients{flex:1}
.tagline{text-align:center;font-size:6.5px;margin-top:4px;color:#999}
.quote{border:1px solid var(--line);padding:8px 10px;margin-top:12px;font-size:7px}
.reviewer{display:flex;align-items:center;gap:10px;margin-top:10px}
.avatar{width:30px;height:30px;border-radius:50%;background:linear-gradient(#c9b7a6,#6d7d95)}
.reviewer strong{display:block;color:var(--heading);font-size:7.5px}
.dots{display:flex;gap:4px;margin-top:6px;padding-left:40px}
.dots span{width:6px;height:6px;background:#bbb}
.dots span:first-child{background:#333}
.client-grid{display:grid;grid-template-columns:repeat(3,1fr);gap:12px 10px;margin-top:18px}
.client{border:1px solid var(--line);height:28px;display:flex;align-items:center;justify-content:center;gap:4px;font-size:8.5px;font-weight:700;color:var(--client)}
.client i{width:7px;height:7px;background:var(--client);display:block}
.newsletter{background:#e4e4e4;height:115px;padding-top:22px}
.signup{display:flex;justify-content:center;gap:12px;margin-top:20px}
.signup span{background:var(--white);border:1px solid var(--line);width:150px;height:22px;font-size:7px;padding:6px 8px;color:#888}
.signup .btn-subscribe{background:var(--navy);color:var(--white);width:70px;text-align:center;font-weight:700;border:none}
.site-footer{background:var(--navy);height:195px;color:#c9d2ea;padding:24px 42px 0;display:flex;gap:26px;position:relative}
.footer-col{flex:1;font-size:6.8px}
.footer-col h4{color:var(--white);font-size:7.5px;font-weight:700;text-transform:uppercase;margin-bottom:8px}
.footer-col li{list-style:none}
.copyright{position:absolute;left:0;right:0;bottom:0;height:20px;background:var(--blue);color:var(--white);text-align:center;font-size:6.5px;line-height:20px}
</style>
</head>
<body>
<header class="site-header">
  <div class="brand"><span class="brand-name">LANTERN</span><span class="brand-tag">INSTITUTE OF BUSINESS &amp; Technology</span></div>
  <div class="account"><span class="btn-sm btn-login">Login</span><span class="btn-sm btn-register">Register Now</span></div>
  <div class="social"><span></span><span></span><span></span></div>
  <nav class="main-nav"><a href="#">Home</a><a href="#">Company</a><a href="#" class="active">Services</a><a href="#">Products</a><a href="#">Demo</a><a href="#">Contact Us</a></nav>
</header>

<section class="hero">
  <div class="hero-photo" role="img" aria-label="Hand touching a glowing network of business and technology icons"></div>
  <div class="hero-content">
    <h1>BUSINESS AND TECHNOLOGY</h1>
    <p>Neque porro quisquam est qui dolorem ipsum quia dolor sit amet</p>
    <div class="hero-actions"><span class="btn btn-dark">Learn More</span><span class="btn btn-orange">Click Here</span></div>
  </div>
</section>

<section class="welcome">
  <h2 class="section-title">Welcome to LIBT</h2>
  <p>Contrary to popular belief, Lorem Ipsum is not simply random text. It has roots in a piece of classical Latin literature from 45 BC, making it over 2000 years old. A Latin scholar at a small college once looked up one of the more obscure Latin words, consectetur, and traced its source.</p>
</section>

<section class="services">
  <h2 class="section-title">Our Services</h2>
  <div class="service-list">
    <div class="service">
      <div class="service-icon"><svg width="20" height="20" viewBox="0 0 20 20"><path d="M2 5h7v11H2zM11 5h7v11h-7z" fill="#fff"/></svg></div>
      <h3>Long Distance Education</h3>
      <p>There are many variations of passages of Lorem Ipsum available, but the majority have suffered alteration in some form.</p>
    </div>
    <div class="service">
      <div class="service-icon highlight"><svg width="20" height="20" viewBox="0 0 20 20"><rect x="2" y="3" width="16" height="10" fill="#fff"/><rect x="8" y="13" width="4" height="3" fill="#fff"/><rect x="5" y="16" width="10" height="2" fill="#fff"/></svg></div>
      <h3 class="highlight">Globalise Information Technology</h3>
      <p>There are many variations of passages of Lorem Ipsum available, but the majority have suffered alteration in some form.</p>
    </div>
    <div class="service">
      <div class="service-icon"><svg width="20" height="20" viewBox="0 0 20 20"><rect x="6" y="2" width="8" height="16" rx="1" fill="#fff"/></svg></div>
      <h3>Direct to Device</h3>
      <p>There are many variations of passages of Lorem Ipsum available, but the majority have suffered alteration in some form.</p>
    </div>
    <div class="service">
      <div class="service-icon"><svg width="20" height="20" viewBox="0 0 20 20"><path d="M10 2l2.4 5 5.4.6-4 3.7 1.1 5.4L10 14l-4.9 2.7 1.1-5.4-4-3.7 5.4-.6z" fill="#fff"/></svg></div>
      <h3>SKILLBRIDGE</h3>
      <p>There are many variations of passages of Lorem Ipsum available, but the majority have suffered alteration in some form.</p>
    </div>
    <div class="service">
      <div class="service-icon"><svg width="20" height="20" viewBox="0 0 20 20"><rect x="3" y="10" width="3" height="7" fill="#fff"/><rect x="8.5" y="6" width="3" height="11" fill="#fff"/><rect x="14" y="3" width="3" height="14" fill="#fff"/></svg></div>
      <h3>Business Verticals</h3>
      <p>There are many variations of passages of Lorem Ipsum available, but the majority have suffered alteration in some form.</p>
    </div>
  </div>
</section>

<section class="feedback">
  <div class="testimonials">
    <h2 class="section-title">Testimonials</h2>
    <p class="tagline">What our students say about their study with us</p>
    <blockquote class="quote">"The courses gave me practical skills and the confidence to apply for new roles. The tutors were helpful and the free online resources made studying easy."</blockquote>
    <div class="reviewer">
      <div class="avatar" role="img" aria-label="Portrait of a student"></div>
      <div><strong>Arin</strong><span>Graduate, business studies programme</span></div>
    </div>
    <div class="dots"><span></span><span></span></div>
  </div>
  <div class="clients">
    <h2 class="section-title">Our Clients</h2>
    <div class="client-grid">
      <div class="client"><i></i>Northwind</div>
      <div class="client"><i></i>Keystone Services</div>
      <div class="client"><i></i>Tallyway</div>
      <div class="client"><i></i>Northwind</div>
      <div class="client"><i></i>Keystone Services</div>
      <div class="client"><i></i>Tallyway</div>
    </div>
  </div>
</section>

<section class="newsletter">
  <h2 class="section-title">Subscribe to Our News Letter</h2>
  <div class="signup"><span>Your Name</span><span>Your Email</span><span class="btn-subscribe">SUBSCRIBE</span></div>
</section>

<footer class="site-footer">
  <div class="footer-col"><h4>LIBT Solutions</h4><p>Contrary to popular belief, Lorem Ipsum is not simply random text. It has roots in a piece of classical Latin literature from 45 BC, making it over 2000 years old.</p></div>
  <div class="footer-col"><h4>About LIBT</h4><ul><li>Company</li><li>Business Sector</li><li>Contact</li></ul></div>
  <div class="footer-col"><h4>Services</h4><ul><li>Long distance education</li><li>Information technology</li><li>Direct to device</li><li>Skillbridge</li><li>Business verticals</li></ul></div>
  <div class="footer-col"><h4>Contact Us</h4><ul><li>48 Harbour Lane,</li><li>Riverside District,</li><li>Eastfield 20415</li><li>Email: info@lanterninstitute.example</li></ul></div>
  <div class="copyright">Copyright © Lantern Institute of Business and Technology. All Rights Reserved.</div>
</footer>
</body>
</html>
```